Unique business card design

Boutique coastal hotel suites - in need of clever stand out business card I have uploaded the logo that I had created through quill forge I want something that is clever and stands out from everyone else - 418 Brantwell Avenue kestrel Harbor 99571 phone or text 907 -581-6142 www.primemarrowbysuites.com

Target Market(s)

Men and woman

Industry/Entity Type

Boutique coastal hotel

Contact Information for Business Card

Marrowby Suites kestrel Harbor marrowby_suites@mailnest.net

Requirements
Must have
• Classy - clever -bold 907-581-6142 call or text

```html
<!DOCTYPE html>
<html lang="en">
<head>
<meta charset="utf-8">
<title>Marrowby Suites – Business Card</title>
<link rel="stylesheet" href="https://fonts.googleapis.com/css2?family=Lato:wght@400;700&display=swap">
<style>
  :root {
    --backdrop: #b3b3b3;
    --card: #ffffff;
    --navy: #2c5172;
    --ink: #2a2a2a;
    --text: #1e1e1e;
    --role: #333333;
    --icon-dark: #2b2b2b;
    --icon-gold: #f4cf3f;
  }
  * { box-sizing: border-box; margin: 0; padding: 0; }
  html, body {
    width: 1200px; height: 1200px; overflow: hidden;
    background: var(--backdrop);
    font-family: "Lato", Arial, sans-serif;
  }
  .card {
    position: absolute; top: 206px;
    width: 451px; height: 788px;
    background: var(--card);
  }
  .card--back { left: 103px; }
  .card--front { left: 646px; }

  .brand {
    position: absolute; left: 0; right: 0;
    display: flex; align-items: center; justify-content: center; gap: 10px;
    color: var(--navy); font-weight: 700;
    font-size: 28px; line-height: 1; letter-spacing: 3px; text-transform: uppercase;
  }
  .brand__mark { width: 16px; height: 16px; background: var(--navy); flex: none; }
  .card--back .brand { top: 380px; }
  .card--front .brand { top: 118px; }

  .person__name {
    position: absolute; left: 0; right: 0; top: 396px;
    font-size: 34px; line-height: 1; font-weight: 700; color: var(--ink); text-align: center;
  }
  .person__role {
    position: absolute; left: 0; right: 0; top: 438px;
    font-size: 19px; line-height: 1; color: var(--role); text-align: center;
  }

  .icons {
    position: absolute; left: 0; right: 0; top: 491px;
    display: flex; justify-content: center; gap: 7px;
  }
  .icons svg { width: 20px; height: 20px; display: block; }

  .line {
    position: absolute; left: 0; right: 0;
    text-align: center; font-size: 18px; line-height: 24px; color: var(--text);
  }
  .address { top: 528px; }
  .phone { top: 589px; }
  .email { top: 626px; }
  .web { top: 660px; }
</style>
</head>
<body>
  <section class="card card--back">
    <div class="brand"><span class="brand__mark"></span>Marrowby Suites</div>
  </section>

  <section class="card card--front">
    <div class="brand"><span class="brand__mark"></span>Marrowby Suites</div>

    <h1 class="person__name">Everett Hale</h1>
    <p class="person__role">Marketing Director</p>

    <div class="icons" aria-hidden="true">
      <svg viewBox="0 0 20 20"><circle cx="10" cy="10" r="10" fill="var(--icon-gold)"/><circle cx="10" cy="10" r="8" fill="var(--icon-dark)"/><path d="M10 15.5c-2.5-3-4-5-4-7a4 4 0 0 1 8 0c0 2-1.5 4-4 7z" fill="none" stroke="var(--icon-gold)" stroke-width="1.3"/><circle cx="10" cy="8.5" r="1.4" fill="var(--icon-gold)"/></svg>
      <svg viewBox="0 0 20 20"><circle cx="10" cy="10" r="10" fill="var(--icon-dark)"/><path d="M6.5 5.5l2 0.2 1 2.5-1.3 1c0.6 1.3 1.5 2.2 2.8 2.8l1-1.3 2.5 1 .2 2c-.3.7-1 1-1.8 1C8.5 14.5 5.5 11.5 5.4 7.2c0-.8.4-1.4 1.1-1.7z" fill="var(--icon-gold)"/></svg>
      <svg viewBox="0 0 20 20"><circle cx="10" cy="10" r="10" fill="var(--icon-dark)"/><path d="M5 10l10-4.5-4 10-1.5-4z" fill="var(--icon-gold)"/></svg>
      <svg viewBox="0 0 20 20"><circle cx="10" cy="10" r="10" fill="var(--icon-dark)"/><g fill="none" stroke="var(--icon-gold)" stroke-width="1.5" stroke-linecap="round"><path d="M9 11l-1.8 1.8a1.8 1.8 0 0 1-2.5-2.5L7 8"/><path d="M11 9l1.8-1.8a1.8 1.8 0 0 1 2.5 2.5L13 12"/><path d="M8.3 11.7l3.4-3.4"/></g></svg>
    </div>

    <p class="line address">418 Brantwell Avenue,<br>kestrel Harbor 99571</p>
    <p class="line phone">907 581 6142</p>
    <p class="line email">marrowby_suites@mailnest.net</p>
    <p class="line web">www.primemarrowbysuites.com</p>
  </section>
</body>
</html>
```